St Louis Electrician Needing a Business Card Design!!

We are a St Louis based electrical contracting firm that needs help designing a business card. We have a logo and I have another image that I would like to incorporate. Open to ideas..Thanks!!

Industry/Entity Type

Business

Requirements
Must have
• there are two downloads...one is the logo and the other is what i was wanting coming off the logo...the light rays. Like the logo with the blue background...Was thinking the whole card would be that color blue.
Should not have
• No lightning bolts

```html
<!DOCTYPE html>
<html lang="en">
<head>
<meta charset="utf-8">
<title>Voltaris Inc. — Business Card</title>
<link rel="stylesheet" href="https://fonts.googleapis.com/css2?family=Questrial&display=swap">
<style>
  :root {
    --page-bg: #e4e6ea;
    --card-blue-light: #1f4f95;
    --card-blue: #183f7c;
    --card-blue-deep: #122f60;
    --text-white: #f1f3f6;
    --text-soft: #d6dce6;
    --accent-cyan: #1fa3dc;
  }
  * { box-sizing: border-box; margin: 0; padding: 0; }
  html, body {
    width: 1200px;
    height: 786px;
    overflow: hidden;
    background: var(--page-bg);
    font-family: "Questrial", "Century Gothic", sans-serif;
  }
  .canvas {
    position: relative;
    width: 1200px;
    height: 786px;
  }
  .business-card {
    position: absolute;
    left: 180px;
    top: 153px;
    width: 840px;
    height: 480px;
    border-radius: 28px;
    background: radial-gradient(ellipse at 45% 30%, var(--card-blue-light) 0%, var(--card-blue) 50%, var(--card-blue-deep) 100%);
    box-shadow: 0 18px 40px rgba(10, 25, 55, 0.25);
    color: var(--text-white);
    overflow: hidden;
  }
  .brand-name {
    position: absolute;
    left: 250px;
    top: 80px;
    font-size: 68px;
    letter-spacing: 0.5px;
    color: var(--text-white);
    line-height: 1;
  }
  .brand-name .brand-suffix {
    font-size: 30px;
    margin-left: 10px;
  }
  .contact-block {
    position: absolute;
    left: 60px;
    top: 250px;
    font-size: 20px;
    line-height: 31px;
    color: var(--text-soft);
    list-style: none;
  }
  .contact-block li {
    display: flex;
    align-items: center;
    gap: 10px;
  }
  .contact-block .no-icon { padding-left: 30px; }
  .contact-icon {
    width: 20px;
    height: 20px;
    flex: none;
  }
  .person {
    position: absolute;
    right: 60px;
    bottom: 58px;
    text-align: right;
  }
  .person-name {
    font-size: 28px;
    letter-spacing: 1.5px;
    text-transform: uppercase;
    color: var(--accent-cyan);
  }
  .person-title {
    margin-top: 6px;
    font-size: 20px;
    color: var(--text-soft);
  }
</style>
</head>
<body>
<main class="canvas">
  <section class="business-card">
    <h1 class="brand-name">Voltaris<span class="brand-suffix">Inc.</span></h1>

    <ul class="contact-block">
      <li class="no-icon">418 Maple Ridge Road</li>
      <li class="no-icon">Ashford, NJ 08740</li>
      <li>
        <svg class="contact-icon" viewBox="0 0 20 20" aria-hidden="true">
          <rect width="20" height="20" rx="3" fill="var(--accent-cyan)"/>
          <path d="M6 4.5c.6-.4 1.3-.3 1.7.3l1 1.6c.3.5.2 1.1-.2 1.4l-.8.6c.5 1.3 1.5 2.4 2.8 3l.6-.8c.3-.4 1-.5 1.4-.2l1.6 1c.6.4.7 1.1.3 1.7l-.6.8c-.6.7-1.6.9-2.5.5C8.4 13.3 6.4 11.2 5.3 8.3c-.4-.9-.1-1.9.6-2.5z" fill="var(--card-blue-deep)"/>
        </svg>
        (555) 014-2290
      </li>
      <li>
        <svg class="contact-icon" viewBox="0 0 20 20" aria-hidden="true">
          <rect width="20" height="20" rx="3" fill="var(--accent-cyan)"/>
          <rect x="4" y="6" width="12" height="8.5" rx="1" fill="none" stroke="var(--card-blue-deep)" stroke-width="1.5"/>
          <path d="M4.5 6.5 10 11l5.5-4.5" fill="none" stroke="var(--card-blue-deep)" stroke-width="1.5"/>
        </svg>
        info@voltarisgroup.com
      </li>
      <li>
        <svg class="contact-icon" viewBox="0 0 20 20" aria-hidden="true">
          <rect width="20" height="20" rx="3" fill="var(--accent-cyan)"/>
          <circle cx="10" cy="10" r="5.5" fill="none" stroke="var(--card-blue-deep)" stroke-width="1.4"/>
          <ellipse cx="10" cy="10" rx="2.3" ry="5.5" fill="none" stroke="var(--card-blue-deep)" stroke-width="1.2"/>
          <path d="M4.5 10h11" stroke="var(--card-blue-deep)" stroke-width="1.2"/>
        </svg>
        www.voltarisgroup.com
      </li>
    </ul>

    <div class="person">
      <p class="person-name">Dana Whitfield</p>
      <p class="person-title">General Manager</p>
    </div>
  </section>
</main>
</body>
</html>
```